Direct Response Landing Page for Paid Search Campaigns for TrailKeepers.com

TrailKeepers.com is a leading people search / public records company, providing consumers with instant, accurate access to public records. We are a direct response org focused on engaging the user and converting the user to a customer. Our product returns instant search results based on a name or phone search. We are looking for a landing page to test out, against our current "Home Page." We will drive traffic to this page via paid search terms (ie., "people search, find people"). We would like a landing page with a headline, search forms, CTA Search button, with features/beneifts about the service and company. Specific Key Messaging will be provided.

Target Market(s)

Consumers. Skew slightly female, ages 40+

Industry/Entity Type

It Company

Number of Pages Required

1 page

Font styles to use
Sans Serif

Requirements
Must have
• Use of Logo; upper left corner, consistent w/ TrailKeepers.com.
• Use of two HTML search forms (prefer a toggle between the two). Users must type in a search query in a search form for either:
• 1. First Name, Last Name, City, State
• 2. Phone # (area code w/ phone #)
• Call to Action: "Search" button
Should not have
• Should not include TrailKeepers.com's standard nav at the top.

```html
<!DOCTYPE html>
<html lang="en">
<head>
<meta charset="utf-8">
<title>TrailKeepers.com – People Search Landing Page</title>
<link rel="stylesheet" href="https://fonts.googleapis.com/css2?family=Open+Sans:wght@400;600;700&display=swap">
<style>
  :root {
    --stage: #e6e7e9;
    --page: #ffffff;
    --brand-blue: #2b7fc1;
    --button-blue: #1f6fae;
    --green: #8cc63f;
    --tab-dark: #5f9a3a;
    --text: #333333;
    --muted: #8a8f94;
    --field-border: #cfd3d6;
    --figure: #d9dcde;
    --icon-green: #3e9b47;
    --social: #6f8fb8;
  }
  * { box-sizing: border-box; margin: 0; padding: 0; }
  html, body { width: 950px; height: 1200px; overflow: hidden; }
  body {
    background: var(--stage);
    font-family: "Open Sans", Arial, sans-serif;
    color: var(--text);
    position: relative;
  }
  .landing-page {
    position: absolute;
    left: 25px; top: 270px;
    width: 900px; height: 660px;
    background: var(--page);
    box-shadow: 0 2px 10px rgba(0,0,0,0.12);
    overflow: hidden;
  }
  .crowd-illustration {
    position: absolute;
    left: 416px; top: 100px;
    width: 484px; height: 560px;
    background: radial-gradient(ellipse at 55% 60%, var(--figure) 0%, rgba(217,220,222,0.55) 45%, rgba(255,255,255,0) 75%);
  }
  .brand-name {
    position: absolute; left: 78px; top: 40px;
    font-size: 34px; font-weight: 600; color: var(--brand-blue);
    line-height: 1;
  }
  .brand-tagline {
    position: absolute; left: 80px; top: 82px;
    font-size: 13px; color: var(--muted); letter-spacing: 0.3px;
  }
  .account-actions {
    position: absolute; left: 660px; top: 56px;
    display: flex; gap: 8px;
  }
  .account-button {
    background: var(--button-blue); color: #fff;
    font-size: 10px; font-weight: 700; text-transform: uppercase;
    padding: 5px 10px; letter-spacing: 0.4px;
  }
  .social-links {
    position: absolute; left: 660px; top: 88px;
    display: flex; gap: 6px;
  }
  .social-square { width: 20px; height: 20px; background: var(--social); }
  .headline {
    position: absolute; left: 78px; top: 198px;
    font-size: 16px; font-weight: 600; color: var(--brand-blue);
    text-transform: uppercase; letter-spacing: 0.2px;
  }
  .search-panel { position: absolute; left: 78px; top: 230px; width: 480px; }
  .search-tabs { display: flex; gap: 4px; }
  .search-tab {
    font-size: 11px; color: #fff; padding: 5px 18px;
    background: var(--tab-dark);
    clip-path: polygon(8px 0, calc(100% - 8px) 0, 100% 100%, 0 100%);
  }
  .search-tab.is-active { background: var(--green); }
  .search-row { display: flex; }
  .search-field {
    flex: 1; height: 30px; border: 1px solid var(--field-border);
    font: 13px "Open Sans", Arial, sans-serif; color: var(--muted);
    padding: 0 10px; display: flex; align-items: center;
  }
  .search-button {
    width: 116px; height: 30px; border: 0;
    background: var(--green); color: #fff;
    font: 700 12px "Open Sans", Arial, sans-serif; letter-spacing: 0.6px;
  }
  .section-title {
    position: absolute; left: 78px;
    font-size: 15px; font-weight: 700; color: var(--brand-blue);
    text-transform: uppercase;
  }
  .who-title { top: 356px; }
  .how-title { top: 468px; }
  .who-list {
    position: absolute; left: 78px; top: 382px;
    list-style: none; font-size: 12.5px; line-height: 21px;
  }
  .who-list li::before { content: "•"; margin-right: 8px; }
  .help-list {
    position: absolute; left: 78px; top: 498px;
    list-style: none; width: 460px;
  }
  .help-item {
    display: flex; align-items: flex-start; gap: 16px;
    font-size: 12.5px; font-weight: 600; line-height: 17px;
    margin-bottom: 14px;
  }
  .help-item svg { flex: 0 0 30px; }
</style>
</head>
<body>
  <main class="landing-page">
    <div class="crowd-illustration" role="img" aria-label="Faint illustration of a hand arranging a crowd of people figures"></div>

    <p class="brand-name">TrailKeepers</p>
    <p class="brand-tagline">records made simple</p>

    <nav class="account-actions">
      <span class="account-button">Signup</span>
      <span class="account-button">Register</span>
    </nav>
    <div class="social-links">
      <span class="social-square"></span><span class="social-square"></span><span class="social-square"></span><span class="social-square"></span><span class="social-square"></span>
    </div>

    <h1 class="headline">Since 1999, your trusted online people search source</h1>

    <form class="search-panel">
      <div class="search-tabs">
        <span class="search-tab is-active">Search by Name</span>
        <span class="search-tab">Search by Phone</span>
      </div>
      <div class="search-row">
        <span class="search-field">First Name, Last Name, City, State*</span>
        <button class="search-button" type="button">SEARCH</button>
      </div>
    </form>

    <h2 class="section-title who-title">Who we are</h2>
    <ul class="who-list">
      <li>Launched online in 1999</li>
      <li>Leading Data-as-a-Service Public Records Organization</li>
      <li>Privacy and Security are paramount to our Organization</li>
    </ul>

    <h2 class="section-title how-title">How we help</h2>
    <ul class="help-list">
      <li class="help-item">
        <svg width="30" height="30" viewBox="0 0 30 30" aria-hidden="true"><circle cx="15" cy="15" r="11" fill="none" stroke="var(--icon-green)" stroke-width="2.5"/><path d="M15 9v6l4 3" fill="none" stroke="var(--icon-green)" stroke-width="2.5" stroke-linecap="round"/></svg>
        <span>TrailKeepers has people, phone, background, property and criminal, at your fingertips</span>
      </li>
      <li class="help-item">
        <svg width="30" height="30" viewBox="0 0 30 30" aria-hidden="true"><path d="M11 5h8l-3 5h-2z" fill="var(--icon-green)"/><ellipse cx="15" cy="19" rx="10" ry="9" fill="var(--icon-green)"/><path d="M18 15.5c-1-1-5-1.2-5 .8s5 1.2 5 3.4-4 2-5.5.8M15 13v11" fill="none" stroke="#fff" stroke-width="1.6"/></svg>
        <span>We do the vetting for you to access local, state and nationwide records = delivering you AFFORDABLE UNLIMITED access.</span>
      </li>
      <li class="help-item">
        <svg width="30" height="30" viewBox="0 0 30 30" aria-hidden="true"><path d="M15 3l10 4v7c0 7-5 11-10 13C10 25 5 21 5 14V7z" fill="var(--icon-green)"/><path d="M10 15l4 4 7-8" fill="none" stroke="#fff" stroke-width="2.5" stroke-linecap="round" stroke-linejoin="round"/></svg>
        <span>We Provide Instant Access to Billions of People Search &amp; Background Records</span>
      </li>
    </ul>
  </main>
</body>
</html>
```